Redesign a Shopify Banner for a spiritual streetwear brand

Redesign Shopify banner for a brand called Vorel Studios we are a spiritually inspired streetwear brand that makes lots of designs with spiritual symbols and space aesthetics like stars. I would like the banner redesigned with the star print I included in this file in the background of the banner with our logo and tag line "spiritually inspired streetwear". you can choose a new font for the banner that could be more aesthetically pleasing. you could also included other alchemical and occult or witchy symbols on the banner along with the stars. or just create the banner with the stars I included in this file. Looking forward to see your work! Thank You.
our website right now is vorel-studios.example

```html
<!DOCTYPE html>
<html lang="en">
<head>
<meta charset="utf-8">
<title>Vorel Studios — Shop Banner</title>
<link rel="stylesheet" href="https://fonts.googleapis.com/css2?family=Cormorant+Garamond:ital,wght@0,700;1,400&display=swap">
<style>
  :root {
    --page-bg: #e4e1e2;
    --banner-ink: #000000;
    --banner-line: #ffffff;
    --placeholder: #2a2a2a;
  }
  html, body {
    margin: 0;
    width: 1200px;
    height: 1200px;
    overflow: hidden;
    background: var(--page-bg);
  }
  .banner {
    position: absolute;
    left: 63px;
    top: 421px;
    width: 1074px;
    height: 357px;
    background: var(--banner-ink);
    color: var(--banner-line);
    box-shadow: 0 4px 8px rgba(0, 0, 0, 0.35);
    overflow: hidden;
  }
  .star-field {
    position: absolute;
    inset: 0;
    width: 1074px;
    height: 357px;
    fill: var(--banner-line);
  }
  .star-field .hollow {
    fill: none;
    stroke: var(--banner-line);
    stroke-width: 1.4;
  }
  .banner-frame {
    position: absolute;
    left: 38px;
    top: 30px;
    width: 1000px;
    height: 304px;
    border: 1px solid var(--banner-line);
    box-sizing: border-box;
  }
  .art {
    position: absolute;
    background: radial-gradient(circle at 50% 50%, #3a3a3a 0%, var(--placeholder) 70%);
    border-radius: 14px;
  }
  .art-potion { left: 130px; top: 82px; width: 128px; height: 193px; }
  .art-crystal-ball { left: 785px; top: 76px; width: 180px; height: 199px; border-radius: 50% 50% 16px 16px; }
  .brand-name {
    position: absolute;
    left: 300px;
    top: 84px;
    width: 474px;
    text-align: center;
    font-family: "Cormorant Garamond", serif;
    font-weight: 700;
    color: var(--banner-line);
    margin: 0;
    line-height: 1;
  }
  .brand-name .word-main { display: block; font-size: 88px; letter-spacing: 6px; line-height: 80px; }
  .brand-name .word-sub { display: block; font-size: 44px; letter-spacing: 14px; margin-top: 26px; padding-left: 14px; }
  .tagline {
    position: absolute;
    left: 0;
    right: 0;
    top: 262px;
    text-align: center;
    font-family: "Cormorant Garamond", serif;
    font-style: italic;
    font-weight: 400;
    font-size: 40px;
    color: var(--banner-line);
    margin: 0;
  }
</style>
</head>
<body>
  <section class="banner">
    <svg class="star-field" viewBox="0 0 1074 357" aria-hidden="true">
      <defs>
        <path id="sparkle" d="M0,-6 Q0,0 6,0 Q0,0 0,6 Q0,0 -6,0 Q0,0 0,-6Z"/>
      </defs>
      <use href="#sparkle" x="514" y="6"/>
      <use href="#sparkle" x="1060" y="7"/>
      <use href="#sparkle" x="7" y="160"/>
      <use href="#sparkle" x="30" y="248"/>
      <use href="#sparkle" x="85" y="343"/>
      <use href="#sparkle" x="311" y="347"/>
      <use href="#sparkle" x="628" y="345"/>
      <use href="#sparkle" x="859" y="347"/>
      <use href="#sparkle" x="818" y="89" transform="translate(818 89) scale(0.8) translate(-818 -89)"/>
      <path class="hollow" d="M33,113 Q33,124 40,124 Q33,124 33,135 Q33,124 26,124 Q33,124 33,113Z"/>
      <g>
        <circle cx="13" cy="5" r="1.8"/>
        <circle cx="100" cy="2" r="1.8"/>
        <circle cx="152" cy="9" r="1.8"/>
        <circle cx="186" cy="22" r="1.8"/>
        <circle cx="245" cy="2" r="1.8"/>
        <circle cx="280" cy="5" r="1.8"/>
        <circle cx="480" cy="2" r="1.8"/>
        <circle cx="782" cy="5" r="1.8"/>
        <circle cx="15" cy="52" r="1.8"/>
        <circle cx="16" cy="86" r="1.8"/>
        <circle cx="12" cy="212" r="1.8"/>
        <circle cx="21" cy="299" r="1.8"/>
        <circle cx="40" cy="353" r="1.8"/>
        <circle cx="148" cy="355" r="1.8"/>
        <circle cx="273" cy="340" r="1.8"/>
        <circle cx="694" cy="340" r="1.8"/>
        <circle cx="1055" cy="69" r="1.8"/>
        <circle cx="1055" cy="113" r="1.8"/>
        <circle cx="1058" cy="167" r="1.8"/>
        <circle cx="1056" cy="206" r="1.8"/>
        <circle cx="1053" cy="249" r="1.8"/>
        <circle cx="1053" cy="299" r="1.8"/>
        <circle cx="1055" cy="355" r="1.8"/>
      </g>
    </svg>
    <div class="banner-frame"></div>
    <div class="art art-potion" role="img" aria-label="Line illustration of a corked potion bottle with a star label"></div>
    <h1 class="brand-name"><span class="word-main">VOREL</span><span class="word-sub">STUDIOS</span></h1>
    <div class="art art-crystal-ball" role="img" aria-label="Line illustration of a crystal ball on a stand with an eye and orbit ring"></div>
    <p class="tagline">Spiritually Inspired Streetwear</p>
  </section>
</body>
</html>
```